Business Card for Technology Startup

Design a 2-sided business card using the logo provided. We are a digital healthcare platform that provides a mobile app and web UI that helps caregivers, families, and doctors share information and provide better patient outcomes. We use AI and machine learning to help guide patients through their day-to-day life. The final design should communicate stability, peace, comfort, but also align with the image of an AI-driven technology startup.

I'd like the deliverable to by a Photoshop PSD file (with layers) that I can work with in pixlr.com. Should contain the following editable layers:
Name (ex. John Doe)
Title (ex. Founder / CEO)
Email (ex. info@brenvaxa.ai)
Phone (ex. (555) 014-2368)
Website (ex. https://brenvaxa.ai)

```html
<!DOCTYPE html>
<html lang="en">
<head>
<meta charset="UTF-8">
<title>Brenvaxa Business Card</title>
<link href="https://fonts.googleapis.com/css2?family=Poppins:wght@400;500;700&display=swap" rel="stylesheet">
<style>
  :root {
    --bg: #2a2a2a;
    --card: #0c0c0d;
    --card-edge: #161617;
    --accent: #29b6e6;
    --white: #ffffff;
    --muted: #e8e8e8;
  }
  * { margin: 0; padding: 0; box-sizing: border-box; }
  html, body { width: 1200px; height: 800px; overflow: hidden; background: var(--bg); }
  body { position: relative; font-family: 'Poppins', sans-serif; }

  .card {
    position: absolute;
    width: 525px;
    height: 300px;
    background: var(--card);
    border-radius: 18px;
    border: 1px solid var(--card-edge);
  }
  .card--front { left: 45px; top: 110px; }
  .card--back { left: 630px; top: 390px; }

  .wordmark {
    font-weight: 700;
    color: var(--white);
    letter-spacing: 0.5px;
    line-height: 1;
    white-space: nowrap;
  }
  .card--front .wordmark {
    position: absolute;
    left: 48px;
    bottom: 52px;
    font-size: 46px;
  }

  .brand {
    position: absolute;
    left: 44px;
    top: 152px;
    display: flex;
    align-items: center;
    gap: 10px;
  }
  .brand__dot {
    width: 18px; height: 18px;
    border-radius: 50%;
    background: var(--accent);
    flex: none;
  }
  .card--back .wordmark { font-size: 34px; }

  .contact {
    position: absolute;
    left: 300px;
    top: 52px;
  }
  .contact__name {
    font-weight: 700;
    font-size: 30px;
    color: var(--accent);
    line-height: 1.1;
    white-space: nowrap;
  }
  .contact__title {
    font-weight: 500;
    font-size: 17px;
    color: var(--white);
    margin-bottom: 22px;
    white-space: nowrap;
  }
  .contact__list { list-style: none; }
  .contact__item {
    display: flex;
    align-items: center;
    gap: 10px;
    font-size: 15px;
    color: var(--muted);
    margin-bottom: 6px;
    white-space: nowrap;
  }
  .contact__icon { width: 14px; height: 14px; fill: var(--accent); flex: none; }
</style>
</head>
<body>
  <section class="card card--front">
    <div class="wordmark">brenvaxa</div>
  </section>

  <section class="card card--back">
    <div class="brand">
      <span class="brand__dot"></span>
      <span class="wordmark">brenvaxa</span>
    </div>

    <div class="contact">
      <div class="contact__name">John Doe</div>
      <div class="contact__title">Founder / CEO</div>
      <ul class="contact__list">
        <li class="contact__item">
          <svg class="contact__icon" viewBox="0 0 16 16"><path d="M3.5 1h3l1.5 4-2 1.3a8.5 8.5 0 0 0 3.7 3.7L11 8l4 1.5v3A2.5 2.5 0 0 1 12.5 15C6.7 15 1 9.3 1 3.5A2.5 2.5 0 0 1 3.5 1z"/></svg>
          (555) 014-2368
        </li>
        <li class="contact__item">
          <svg class="contact__icon" viewBox="0 0 16 16"><path d="M15 1 1 7l5.5 2L15 1 8 10.5 10 15z"/></svg>
          info@brenvaxa.ai
        </li>
        <li class="contact__item">
          <svg class="contact__icon" viewBox="0 0 16 16"><path d="M8 1a7 7 0 1 0 0 14A7 7 0 0 0 8 1zm0 1.5c.9 0 1.9 1.7 2.2 4.5H5.8C6.1 4.2 7.1 2.5 8 2.5zM2.6 7h1.7c.1-1.4.4-2.7.9-3.7A5.5 5.5 0 0 0 2.6 7zm0 2a5.5 5.5 0 0 0 2.6 3.7c-.5-1-.8-2.3-.9-3.7zm3.2 0h4.4c-.3 2.8-1.3 4.5-2.2 4.5S6.1 11.8 5.8 9zm5.9 0c-.1 1.4-.4 2.7-.9 3.7A5.5 5.5 0 0 0 13.4 9zm1.7-2a5.5 5.5 0 0 0-2.6-3.7c.5 1 .8 2.3.9 3.7z"/></svg>
          www.brenvaxa.ai
        </li>
      </ul>
    </div>
  </section>
</body>
</html>
```